What happens?

Develop a graphic to be used on a church web page based on the following:

"What happens at the intersection of spirituality, sexuality and social justice?"
A second graphic will use the first concept and add an answer to it. "healing, creativity, acceptance, forgiveness, wholeness, service, freedom."

The graphic should be shades of gray, possibly with touches of color (yellow and blue).
This design needs to convey the idea of intersection not just be text.

Attached is a very rough graphic concept to use as a starting point.

Target Market(s)

young adults interested in progressive spirituality rather than dogmatic religion

Industry/Entity Type

Church

Font styles to use
Sans Serif

Requirements
Must have
• visual concept of intersection, visually tying of the answers to the question
Should not have
• just text

```html
<!DOCTYPE html>
<html lang="en">
<head>
<meta charset="utf-8">
<title>What happens at the intersection?</title>
<link rel="stylesheet" href="https://fonts.googleapis.com/css2?family=Arimo:wght@400&display=swap">
<style>
  :root {
    --ink: #0a0a0a;
    --accent-blue: #1f48ff;
    --bg-center: #f7f7f7;
    --bg-mid: #d6d6d8;
    --bg-edge: #a7a7a9;
    --gold-center: #fff7dc;
    --gold-mid: #ffe083;
    --gold-edge: #fbbb12;
    --ring: rgba(255,255,255,0.55);
    --ring-dark: rgba(120,120,125,0.28);
  }
  html, body {
    margin: 0;
    padding: 0;
    width: 792px;
    height: 1200px;
    overflow: hidden;
  }
  .poster {
    display: block;
    width: 792px;
    height: 1200px;
    font-family: "Arimo", "Helvetica Neue", Arial, sans-serif;
  }
  .question-line { fill: var(--ink); font-weight: 400; }
  .theme-word { fill: var(--accent-blue); font-weight: 400; }
  .answer-word { fill: var(--ink); font-weight: 400; }
  .venn-ring { fill: none; stroke: var(--ring-dark); stroke-width: 2; }
  .venn-ring-light { fill: none; stroke: var(--ring); stroke-width: 2; }
  .connector { fill: none; stroke: var(--ring-dark); stroke-width: 2; }
  .connector-tip { fill: var(--gold-edge); }
</style>
</head>
<body>
<svg class="poster" viewBox="0 0 792 1200" xmlns="http://www.w3.org/2000/svg" role="img" aria-label="What happens at the intersection of spirituality, sexuality and social justice? Healing, creativity, innovation, growth.">
  <defs>
    <radialGradient id="bgGlow" cx="50%" cy="33%" r="75%">
      <stop offset="0%" stop-color="var(--bg-center)"/>
      <stop offset="50%" stop-color="var(--bg-mid)"/>
      <stop offset="100%" stop-color="var(--bg-edge)"/>
    </radialGradient>
    <radialGradient id="goldGlow" cx="50%" cy="50%" r="62%">
      <stop offset="0%" stop-color="var(--gold-center)"/>
      <stop offset="55%" stop-color="var(--gold-mid)"/>
      <stop offset="100%" stop-color="var(--gold-edge)"/>
    </radialGradient>
    <filter id="whiteGlow" x="-10%" y="-30%" width="120%" height="160%">
      <feGaussianBlur in="SourceAlpha" stdDeviation="5" result="blur"/>
      <feFlood flood-color="#ffffff" flood-opacity="1"/>
      <feComposite in2="blur" operator="in" result="glow"/>
      <feMerge>
        <feMergeNode in="glow"/>
        <feMergeNode in="glow"/>
        <feMergeNode in="SourceGraphic"/>
      </feMerge>
    </filter>
    <filter id="boxShadow" x="-10%" y="-10%" width="120%" height="125%">
      <feDropShadow dx="0" dy="12" stdDeviation="9" flood-color="#000" flood-opacity="0.5"/>
    </filter>
  </defs>

  <rect class="background" width="792" height="1200" fill="url(#bgGlow)"/>

  <g class="intersection-motif">
    <circle class="venn-ring" cx="300" cy="300" r="230"/>
    <circle class="venn-ring" cx="492" cy="300" r="230"/>
    <circle class="venn-ring" cx="396" cy="440" r="230"/>
    <circle class="venn-ring-light" cx="300" cy="302" r="230"/>
    <circle class="venn-ring-light" cx="492" cy="302" r="230"/>
    <circle class="venn-ring-light" cx="396" cy="442" r="230"/>
    <path class="connector" d="M396 580 L396 612"/>
    <path class="connector-tip" d="M384 608 L408 608 L396 622 Z"/>
  </g>

  <g class="question" filter="url(#whiteGlow)">
    <text class="question-line" x="78" y="160" font-size="104" textLength="648" lengthAdjust="spacingAndGlyphs">What happens</text>
    <text class="question-line" x="80" y="233" font-size="66" textLength="640" lengthAdjust="spacingAndGlyphs">at the intersection of</text>
    <text class="theme-word" x="78" y="320" font-size="112" textLength="650" lengthAdjust="spacingAndGlyphs">spirituality,</text>
    <text class="theme-word" x="78" y="433" font-size="112" textLength="640" lengthAdjust="spacingAndGlyphs">sexuality</text>
    <text class="question-line" x="80" y="556" font-size="86" textLength="642" lengthAdjust="spacingAndGlyphs">and social justice?</text>
  </g>

  <rect class="answer-panel" x="76" y="622" width="663" height="478" fill="url(#goldGlow)" filter="url(#boxShadow)"/>

  <g class="answers" filter="url(#whiteGlow)">
    <text class="answer-word" x="108" y="740" font-size="127" textLength="584" lengthAdjust="spacingAndGlyphs">HEALING</text>
    <text class="answer-word" x="105" y="841" font-size="100" textLength="585" lengthAdjust="spacingAndGlyphs">CREATIVITY</text>
    <text class="answer-word" x="110" y="951" font-size="104" textLength="580" lengthAdjust="spacingAndGlyphs">INNOVATION</text>
    <text class="answer-word" x="105" y="1068" font-size="125" textLength="587" lengthAdjust="spacingAndGlyphs">GROWTH</text>
  </g>
</svg>
</body>
</html>
```